2 business Banners for trade show - Transportation industry

Design 2 roll up banners for trade show and career show
-Size: 80 cm X 200 cm each banner
-Will provide text once the design is selected, please use dummy text first. Regarding the text, the first banner will show 6-7 highlights of the company services. The second banner will have around 50 words brief instruction of the company.
-Use the logo in attachment.
-You can use Microgamma font or a similar font Eurostile and Coda in Google Fonts.
-We are looking for simple and clean design and should match the theme colour of the logo.
-You may use the images that align with our business (Such as air cargo transport, ocean cargo transport, on road trucking, rail cargo transport, customs brokerage and e-commerce transport)
-Refer to the company website for more information http://www.vormelfreight.example Note that do NOT follow the design of the website as it will be updated soon.
-Winner will be hired for more works such as web design

Target Market(s)

Business and corporations

Industry/Entity Type

Logistics

Font styles to use
Other font styles liked:
• Microgamma

Requirements
Must have
• -Match the theme colour of the logo in attachment
Nice to have
• -Transportation images that align with the company's services
Should not have
• -Should not contain images of people
• -Should not follow the design of our existing company website

```html
<!DOCTYPE html>
<html lang="en">
<head>
<meta charset="utf-8">
<title>Vormel Freight – Roll-up Banners</title>
<link rel="stylesheet" href="https://fonts.googleapis.com/css2?family=Roboto+Condensed:wght@400;700&family=Michroma&display=swap">
<style>
  :root {
    --bg: #d9d9d9;
    --paper: #ffffff;
    --red: #d2202f;
    --dark: #2b2b2d;
    --placeholder: #c4c4c4;
  }
  * { margin: 0; padding: 0; box-sizing: border-box; }
  html, body { width: 1200px; height: 1126px; overflow: hidden; }
  body {
    background: var(--bg);
    position: relative;
    font-family: "Roboto Condensed", Arial, sans-serif;
  }
  .banner {
    position: absolute;
    top: 63px;
    width: 400px;
    height: 1000px;
    background: var(--paper);
    box-shadow: 0 10px 30px rgba(0,0,0,0.18);
    overflow: hidden;
  }
  .banner--services { left: 150px; }
  .banner--about { left: 650px; }

  .brand {
    position: absolute;
    top: 62px;
    left: 0;
    width: 100%;
    display: flex;
    justify-content: center;
    align-items: center;
    gap: 12px;
  }
  .brand__mark {
    width: 22px;
    height: 22px;
    background: var(--red);
  }
  .brand__name {
    font-family: "Roboto Condensed", Arial, sans-serif;
    font-weight: 700;
    font-size: 46px;
    line-height: 1;
    color: var(--dark);
    letter-spacing: 0.5px;
  }
  .rule {
    position: absolute;
    top: 168px;
    left: 0;
    width: 100%;
    height: 8px;
    background: var(--dark);
  }
  .tagline {
    position: absolute;
    top: 176px;
    width: 300px;
    height: 88px;
    background: var(--red);
    color: #fff;
    font-weight: 700;
    font-size: 27px;
    line-height: 1.1;
    text-align: center;
    display: flex;
    align-items: center;
    justify-content: center;
    text-transform: uppercase;
  }
  .banner--services .tagline { left: 46px; }
  .banner--about .tagline { left: 36px; }

  .placeholder {
    position: absolute;
    top: 365px;
    left: 0;
    width: 100%;
    text-align: center;
    font-weight: 700;
    font-size: 32px;
    line-height: 1.25;
    color: var(--placeholder);
    text-transform: uppercase;
  }
  .swoosh {
    position: absolute;
    top: 556px;
    left: 0;
    width: 400px;
    height: 50px;
    display: block;
  }
  .photo {
    position: absolute;
    top: 598px;
    left: 0;
    width: 100%;
    height: 318px;
  }
  .photo--freight {
    background: linear-gradient(160deg, #2c3f63 0%, #6a5566 30%, #c0603a 55%, #8e2f24 78%, #4a3a36 100%);
  }
  .photo--port {
    background: linear-gradient(170deg, #8aa6b8 0%, #e7b15e 30%, #d9782f 55%, #6e3c28 80%, #2e2a2a 100%);
  }
  .footer-stripe {
    position: absolute;
    top: 916px;
    left: 0;
    width: 100%;
    height: 8px;
    background: var(--red);
  }
  .url {
    position: absolute;
    top: 948px;
    left: 0;
    width: 100%;
    text-align: center;
    font-family: "Michroma", Arial, sans-serif;
    font-size: 14px;
    color: var(--dark);
    letter-spacing: 0.5px;
  }
</style>
</head>
<body>

  <section class="banner banner--services">
    <div class="brand">
      <span class="brand__mark"></span>
      <span class="brand__name">Vormel Freight</span>
    </div>
    <div class="rule"></div>
    <div class="tagline">Your cargo<br>we care</div>
    <p class="placeholder">Your text<br>here</p>
    <svg class="swoosh" viewBox="0 0 400 50" aria-hidden="true">
      <path d="M0 6 Q200 22 400 18 L400 42 L0 42 Z" fill="var(--red)"/>
      <path d="M300 12 Q360 6 400 2 L400 10 Q350 14 300 14 Z" fill="var(--dark)"/>
      <path d="M0 26 Q200 40 400 36 L400 50 L0 50 Z" fill="var(--paper)"/>
    </svg>
    <div class="photo photo--freight" role="img" aria-label="Air, container and truck freight scene at sunset"></div>
    <div class="footer-stripe"></div>
    <p class="url">www.vormelfreight.example</p>
  </section>

  <section class="banner banner--about">
    <div class="brand">
      <span class="brand__mark"></span>
      <span class="brand__name">Vormel Freight</span>
    </div>
    <div class="rule"></div>
    <div class="tagline">Greater visibility<br>and control</div>
    <p class="placeholder">Your text<br>here</p>
    <svg class="swoosh" viewBox="0 0 400 50" aria-hidden="true">
      <path d="M0 24 Q200 30 400 0 L400 26 Q200 44 0 44 Z" fill="var(--dark)"/>
      <path d="M0 48 Q200 44 400 30 L400 36 Q200 50 0 50 Z" fill="var(--red)"/>
    </svg>
    <div class="photo photo--port" role="img" aria-label="Container ship and port cranes at sunset"></div>
    <div class="footer-stripe"></div>
    <p class="url">www.vormelfreight.example</p>
  </section>

</body>
</html>
```